Australia-Wide Industry Leader Bookkeeping Business Website Design Required

We need a website designed for our 10 year old bookkeeping business, Linden & Crane. Linden & Crane has been servicing the local & interstate communities of Australia, providing first-class BAS & Bookkeeping services with a personal touch unmatched by anyone else in the county.

What began 10 years ago as a small business focusing on family, friends and the local community, it has since grown into a well respected business with 95% of their business based solely on word of mouth and personal referrals from around Australia.

We would like to see designs that incorporate our existing brand/logo. The colours to be used on the website should be colours that work well with our logo. The design should communicate maturity, trust and confidence with a Web 2.0 look and feel.

We have produced mockups of the entire website as well as assets used in the mockups. Please reference the attached files. The mockups are an example of all the design elements that we want on each page. Designers are encouraged to use the mockups as a guideline only and for designers to use their own creativity.
Updates

This message is for new graphic designers who are considering commencing work on this project. Thank you for expressing an interest in our project. We would like to inform you that this project is close to completion as we have a number designs under very serious consideration.

We are currently in a position where we are disinterested providing feedback to improve on new designs submitted. We will provide feedback to improve new designs only if the submitted designs are very close to what we want for our website, and will only require 1 or 2 revision rounds to refine before the project completion date we will not work with designers to refine their newly submitted designs.

We feel that it is important for all designers to know the above information as we feel that your time and effort may be better spent working on another project.

Thank you for your understanding.

A big thank you for all the designs submitted. We are now in the process of selecting a design. Please be patient during this process. Thank you.

Target Market(s)

Busy Business Owners

Industry/Entity Type

Small Business

Requirements
Must have
• We require a rectangular "slide show" type feature to serve as a "teaser" to arouse the emotions of our website visitors. Each slide asks a specific question. The questions are:

- Is your paperwork in a mess?
- Do you need to get organised for the end of financial year?
- Are you sick & tired of endless amounts of paperwork & BASs?
- Do you feel frustrated & annoyed because you know your books need to be done?
- Do you lack the time & patience to get your paperwork done?
- Do you wish you had more time to do the things you enjoy doing?
- Contact Linden & Crane today and we will transform your chaos into order.

Underneath the slide show will be a button to "Call Linden & Crane Now - 03 7482 9163".

```html
<!DOCTYPE html>
<html lang="en">
<head>
<meta charset="utf-8">
<title>Linden &amp; Crane – BAS &amp; Bookkeeping</title>
<link href="https://fonts.googleapis.com/css2?family=Tinos:wght@400;700&family=Arimo:wght@400;700&display=swap" rel="stylesheet">
<style>
:root{
  --red:#7d0505;
  --red-deep:#6a0000;
  --ink:#1c1c1c;
  --grey-top:#9a9a9a;
  --grey-mid:#6e6e6e;
  --grey-band:#dcdcdc;
  --grey-logos:#e2e2e2;
  --footer:#5a5a5a;
  --panel:#4f4f4f;
  --white:#ffffff;
}
*{box-sizing:border-box;margin:0;padding:0}
html,body{width:794px;height:1200px;overflow:hidden}
body{position:relative;background:var(--white);font-family:"Tinos",serif;color:var(--ink)}
.abs{position:absolute}

.header-band{left:0;top:0;width:794px;height:242px;background:linear-gradient(#b8b8b8,#8d8d8d 60%,#6f6f6f)}
.summary-band{left:0;top:242px;width:794px;height:341px;background:var(--grey-band)}

.brand{left:283px;top:5px;width:227px;height:43px;background:var(--white);border:2px solid var(--red-deep);display:flex;align-items:center;justify-content:center;font-family:"Tinos",serif;font-size:27px;color:var(--red);gap:8px}
.brand-mark{width:12px;height:12px;background:var(--red)}

.nav{left:89px;top:57px;width:615px;height:30px;background:linear-gradient(#f4f4f4,#d6d6d6);display:flex;align-items:center;font-family:"Tinos",serif;font-size:8.5px;font-weight:700;color:#7a7a7a;letter-spacing:.3px}
.nav a{text-decoration:none;color:inherit;padding:0 5px}
.nav .current{background:var(--red);color:var(--white);height:30px;line-height:30px;padding:0 11px}
.nav .sep{color:#999}
.search{margin-left:auto;margin-right:4px;display:flex;align-items:center;gap:3px}
.search span{width:120px;height:17px;background:var(--white);border-radius:9px;font-size:8px;color:#aaa;text-align:right;padding:3px 8px;font-weight:400}

.strap{left:89px;top:92px;width:615px;text-align:center;color:var(--white);font-family:"Tinos",serif;font-weight:700;font-size:13.4px;line-height:18.5px;text-transform:uppercase}
.strap q{quotes:"\201C" "\201D";font-size:13.4px}

.welcome{left:89px;top:158px;width:615px;height:241px;background:linear-gradient(90deg,#fff,#e9e9e9);box-shadow:0 1px 3px rgba(0,0,0,.3)}
.welcome h1{position:absolute;left:0;top:0;width:308px;height:45px;background:var(--red);color:var(--white);font-weight:400;font-size:19px;line-height:45px;padding-left:12px}
.slide-q{position:absolute;left:308px;top:0;width:307px;height:45px;background:var(--white);text-align:center;font-size:14.5px;line-height:18px;padding-top:4px;border-bottom:2px solid var(--red)}
.slide-q .accent{color:var(--red)}
.welcome p{position:absolute;left:12px;top:74px;width:288px;font-family:"Arimo",sans-serif;font-size:7.2px;line-height:9.6px;color:#333;text-align:justify}
.slide-img{position:absolute;left:308px;top:47px;width:307px;height:194px;background:radial-gradient(ellipse at 55% 45%,#d8d6d2,#b9b6b0 55%,#8f8c86)}
.dots{position:absolute;right:12px;bottom:8px;display:flex;gap:4px}
.dots i{width:8px;height:8px;border-radius:50%;background:#bdbdbd}
.dots i.on{background:var(--red)}

.tick{position:relative;padding-left:18px}
.tick::before{content:"";position:absolute;left:0;top:1px;width:11px;height:11px;background:var(--red)}
.tick::after{content:"";position:absolute;left:3px;top:2px;width:4px;height:7px;border:solid var(--white);border-width:0 1.6px 1.6px 0;transform:rotate(40deg)}

.summaries h2{position:absolute;left:89px;top:415px;font-weight:400;font-size:19px}
.summaries ul{position:absolute;list-style:none;font-size:11px;line-height:21.8px}
.col-a{left:89px;top:444px}
.col-b{left:295px;top:444px}

.call{left:504px;top:418px;width:200px;height:431px;background:var(--white);box-shadow:0 0 3px rgba(0,0,0,.3)}
.call-head{height:44px;background:var(--red);color:var(--white);display:flex;align-items:center;gap:10px;padding-left:10px;font-size:16px;line-height:17px}
.call-body{height:96px;background:var(--panel);color:var(--white);padding:8px}
.call-body h3{font-weight:400;font-size:16px;color:#e6e6e6}
.call-body p{font-size:6.6px;line-height:8.5px;margin-top:8px;font-weight:700}
.call-body strong{display:block;font-family:"Arimo",sans-serif;font-size:10px;margin-top:6px;letter-spacing:.2px}
.map{height:291px;background:linear-gradient(#f4f4f4,#e2e2e2);position:relative}
.map i{position:absolute;left:30px;top:60px;width:140px;height:150px;background:#3d3d3d;border-radius:40% 45% 35% 40%}

.diff{left:89px;top:597px;width:400px}
.diff h2{font-size:14.5px;color:var(--red);font-weight:700;margin-bottom:22px}
.diff ul{list-style:none;font-size:9px;line-height:13px}
.diff > ul > li{margin-bottom:13px}
.diff .dots-list{list-style:none;margin:5px 0 0 -1px;line-height:12px}
.diff .dots-list li{position:relative;padding-left:18px}
.diff .dots-list li::before{content:"";position:absolute;left:3px;top:4px;width:5px;height:5px;border-radius:50%;background:var(--red)}
.diff .closing{font-size:14.5px;color:var(--red);font-weight:700;margin-top:18px}

.quals{left:503px;top:860px;width:200px}
.quals h3{font-size:10.5px;color:var(--red);font-weight:700;margin-bottom:6px}
.quals ul{list-style:none;font-size:10.3px;font-weight:700;line-height:14.8px}

.partners{left:0;top:1029px;width:794px;height:118px;background:var(--grey-logos)}
.badge{position:absolute;background:#bdbdbd}
.footer{left:0;top:1147px;width:794px;height:53px;background:var(--footer);color:var(--white);font-size:9px}
.footer .follow{position:absolute;left:89px;top:19px;display:flex;align-items:center;gap:6px}
.footer .follow i{width:20px;height:20px;border-radius:50%;background:#3a3a3a}
.footer .follow i.alt{background:var(--red)}
.footer .copy{position:absolute;right:92px;top:24px;font-size:8px}
</style>
</head>
<body>
<div class="abs header-band"></div>
<div class="abs summary-band"></div>

<div class="abs brand"><span class="brand-mark"></span>Linden &amp; Crane</div>

<nav class="abs nav">
  <a class="current">HOME</a><a>ABOUT US</a><span class="sep">|</span><a>SERVICES</a><span class="sep">|</span><a>TESTIMONIALS</a><span class="sep">|</span><a>ARTICLES</a><span class="sep">|</span><a>ENDORSEMENT</a><span class="sep">|</span><a>LINKS</a><span class="sep">|</span><a>CONTACT US</a>
  <div class="search"><span>Search</span>
    <svg width="14" height="14" viewBox="0 0 14 14"><circle cx="6" cy="6" r="4" fill="none" stroke="#fff" stroke-width="2"/><line x1="9" y1="9" x2="13" y2="13" stroke="#fff" stroke-width="2"/></svg>
  </div>
</nav>

<p class="abs strap"><q>For nearly 10 years Linden &amp; Crane has been servicing the local &amp; interstate communites of Australia, providing first-class BAS &amp; bookkeeping services with a personal touch unmatched by anyone else in the country.</q></p>

<section class="abs welcome">
  <h1>Welcome to Linden &amp; Crane</h1>
  <div class="slide-q"><span class="accent">Do you feel frustrated &amp; annoyed because</span><br>you know your books need to be done?</div>
  <p>Having worked for a certified accountant firm for numerous year, Helena Linden &amp; Ruth Crane become concerned about the consistency of inaccurate books prepared by other in various organization. As the quality of bookworm declined, the fees seemed to increased , together they identified a need for a quality bookkeeping that truly understood what being is business is all about &amp; more importantly how to correctly &amp; accurately process book according to the los &amp; requirement set by the Australian taxation office. They wanted to give people a batter alternative- thus Linden &amp; Crane was born, what begin as a small business focusing on family, friend &amp; the local communities, has since grow in to a well respected business with 95% of their business based slowly on word of mouth &amp; personal referrals from around Australia</p>
  <div class="slide-img" role="img" aria-label="Slide photo: a stressed office worker reaching out from a pile of crumpled paperwork">
    <div class="dots"><i></i><i></i><i></i><i class="on"></i><i></i><i></i><i></i></div>
  </div>
</section>

<section class="summaries">
  <h2>To summaries</h2>
  <ul class="col-a">
    <li class="tick">Free initial consulting</li>
    <li class="tick">Register BAS agent &nbsp;#48215-113</li>
    <li class="tick">Bookkeeping</li>
    <li class="tick">BAS preparation &amp; lodgment</li>
    <li class="tick">Pay roll</li>
    <li class="tick">IAS preparation &amp; lodgment</li>
  </ul>
  <ul class="col-b">
    <li class="tick">Superannuation</li>
    <li class="tick">Margined scheme</li>
    <li class="tick">Fuel tax credit</li>
    <li class="tick">Offsite &amp; onsite bookkeeping</li>
    <li class="tick">Ledgerly software &amp; training</li>
    <li class="tick">Australian wide</li>
  </ul>
</section>

<aside class="abs call">
  <div class="call-head">
    <svg width="30" height="30" viewBox="0 0 30 30"><circle cx="15" cy="15" r="13" fill="none" stroke="#fff" stroke-width="2"/><path d="M10 8c1-1 2 0 3 2s0 2-1 3c1 2 3 4 5 5 1-1 1-2 3-1s3 2 2 3c-1 2-3 3-6 1-3-2-5-4-7-7-1-3 0-5 1-6z" fill="#fff"/></svg>
    <div>Call us now<br>03 7482 9163</div>
  </div>
  <div class="call-body">
    <h3>Service all of Australia</h3>
    <p>95% of our clients come from client &amp; accountant referrals. We have client all over Victoria Queensland, NSW &amp; Western Australia</p>
    <strong>SO NO MATTER WHERE YOU ARE WE CAN HELP</strong>
  </div>
  <div class="map" role="img" aria-label="Map of Australia marking client locations by state, with town lists for each state"><i></i></div>
</aside>

<section class="abs diff">
  <h2>What makes Linden &amp; Crane different from other bookkeepers</h2>
  <ul>
    <li class="tick">We guarantee we quality of our work</li>
    <li class="tick">We have owned a operated business for 35 years</li>
    <li class="tick">We have over 35 years of experienced</li>
    <li class="tick">The Linden &amp; Crane team are investors &amp; traders</li>
    <li class="tick">Extensive business network for your benefits</li>
    <li class="tick">Backed by a team of accountants</li>
    <li class="tick">We work with a team of elite accountants &amp; wealth Creation professionals who coach us monthly in the following:
      <ul class="dots-list">
        <li>Assets protection</li>
        <li>superannuation &amp; self managed<br>superannuationfunds</li>
        <li>property investing</li>
        <li>tax steatites, tax structure &amp; best tax saving</li>
      </ul>
    </li>
    <li class="tick">We understand just how important it is to help lead &amp; guide our clients from making profits to:
      <ul class="dots-list">
        <li>Maximum profits</li>
        <li>Wealth creation</li>
        <li>Tax minim station</li>
        <li>Asset protection</li>
      </ul>
    </li>
  </ul>
  <p class="closing">This is something that other bookkeeper just don’t do !</p>
</section>

<section class="abs quals">
  <h3>Qualifications, Membership &amp; Partnership</h3>
  <ul>
    <li class="tick">Register ATO BAS agent</li>
    <li class="tick">Certified IV financial service</li>
    <li class="tick">Certified lll financial services</li>
    <li class="tick">Member of guild of chartered bookkeepers</li>
    <li class="tick">Platinum member of Bookkeepers Alliance</li>
    <li class="tick">Ledgerly professional partner</li>
    <li class="tick">TaxWise Network</li>
  </ul>
</section>

<section class="abs partners" aria-label="Partner badges">
  <div class="badge" style="left:88px;top:17px;width:47px;height:80px"></div>
  <div class="badge" style="left:205px;top:17px;width:71px;height:80px"></div>
  <div class="badge" style="left:335px;top:27px;width:88px;height:66px"></div>
  <div class="badge" style="left:478px;top:33px;width:36px;height:62px"></div>
  <div class="badge" style="left:552px;top:44px;width:152px;height:36px"></div>
</section>

<footer class="abs footer">
  <div class="follow">FOLLOW US ON <i></i><i class="alt"></i></div>
  <div class="copy">© &nbsp;Copyrights 2012 Linden &amp; Crane</div>
</footer>
</body>
</html>
```